Public Adjuster mailing campaign

We are public insurance adjusters. When people (the insured) are not being paid fairly on their insurance claim, we help them get paid all they are owed according to their coverage.We would like a post card mailer to send to homes that have been damaged by a recent tornado. I would like to say something like...Storm Damage?Is your insurance paying everything you are owed?You have rights!Get a FREE claim review!CALL NOW!972-954-6845ADJUSTER FOR THE INSUREDI would like to see a photo in the back ground of a damaged home. I would like a design on both sides of the post card.Colors I prefer are navy as a base color and white text ( or red text for the CALL NOW and the phone number.I would like the message to communicate I am a licensed public adjuster working for the insured and I can help them get what they are owed from the insurance company.

```html
<!DOCTYPE html>
<html lang="en">
<head>
<meta charset="UTF-8">
<title>Storm Damage Postcard</title>
<link href="https://fonts.googleapis.com/css2?family=Mulish:wght@700;800&family=Arimo:wght@700&display=swap" rel="stylesheet">
<style>
  :root {
    --sky: #8fc3e6;
    --sky-deep: #6aa9d9;
    --siding: #8f8e7c;
    --debris: #8a6a4c;
    --lawn: #6f9a4a;
    --navy: #4a5f9e;
    --navy-deep: #3d4f8a;
    --navy-dusk: #5d6aa0;
    --rubble: #8e6f7a;
    --white: #ffffff;
    --red: #e0343a;
  }
  * { margin: 0; padding: 0; box-sizing: border-box; }
  html, body { width: 1200px; height: 856px; overflow: hidden; background: var(--white); }
  .postcard {
    position: relative;
    width: 1200px;
    height: 856px;
    display: flex;
    background: var(--white);
  }
  .photo-front {
    width: 616px;
    height: 100%;
    background: linear-gradient(180deg,
      var(--sky) 0%, var(--sky-deep) 38%,
      var(--debris) 42%, var(--siding) 55%,
      var(--siding) 74%, var(--debris) 82%,
      var(--lawn) 90%, var(--lawn) 100%);
  }
  .divider { width: 3px; height: 100%; background: var(--white); }
  .message-side {
    position: relative;
    flex: 1;
    height: 100%;
    background: linear-gradient(180deg,
      var(--navy) 0%, var(--navy-deep) 30%,
      var(--navy-dusk) 45%, var(--rubble) 70%,
      var(--navy-dusk) 88%, var(--navy-deep) 100%);
    color: var(--white);
    text-align: center;
  }
  .message-side > * { position: absolute; left: 0; right: 0; }
  .headline {
    top: 84px;
    font-family: "Mulish", sans-serif;
    font-weight: 800;
    font-size: 40px;
  }
  .question {
    top: 178px;
    font-family: "Mulish", sans-serif;
    font-weight: 800;
    font-size: 28px;
    line-height: 40px;
  }
  .rights {
    top: 378px;
    font-family: "Arimo", sans-serif;
    font-weight: 700;
    font-size: 28px;
    line-height: 40px;
  }
  .call {
    top: 530px;
    font-family: "Arimo", sans-serif;
    font-weight: 700;
    font-size: 42px;
    line-height: 54px;
    color: var(--red);
  }
  .tagline {
    top: 762px;
    font-family: "Arimo", sans-serif;
    font-weight: 700;
    font-size: 30px;
  }
</style>
</head>
<body>
  <div class="postcard">
    <div class="photo-front" role="img" aria-label="Photograph of a house with its roof torn open by a tornado, snapped trees and debris piled on the lawn"></div>
    <div class="divider"></div>
    <div class="message-side" role="group" aria-label="Storm-damaged home under a dark navy sky, with the postcard message">
      <h1 class="headline">Storm Damage?</h1>
      <p class="question">Is your insurance paying every-<br>thing you are owed?</p>
      <p class="rights">You have rights!<br>Get a FREE claim review!</p>
      <p class="call">CALL NOW!<br>641-387-2290</p>
      <p class="tagline">ADJUSTER FOR THE INSURED</p>
    </div>
  </div>
</body>
</html>
```